Medical Billing - Professional Marketing Flier

We are needing help designing a clean and professional looking easy to read marketing flier for a medical billing practice. The text needs to be large enough to print. We are looking for a 5.5 x 8.5 design that we can edit the text as needed. I have included our logo and what we initially want it to say. Please keep in mind, we also want our logo and contact details on the flier. Let me know if you have any questions.

```html
<!DOCTYPE html>
<html lang="en">
<head>
<meta charset="utf-8">
<title>Lyra Medical Billing – Flier</title>
<link rel="stylesheet" href="https://fonts.googleapis.com/css2?family=Montserrat:wght@400;600&family=Poppins:wght@300&display=swap">
<style>
  :root {
    --backdrop: #9b9a9b;
    --paper: #ffffff;
    --night: #1a1618;
    --night-glow: #3a3236;
    --ink: #1f1f24;
    --heading: #2c3a4f;
    --rule: #b565a7;
    --orchid: #b464a8;
    --violet: #6f63a8;
    --logo: #a77bc0;
    --white: #ffffff;
  }
  * { margin: 0; padding: 0; box-sizing: border-box; }
  html, body { width: 882px; height: 1200px; overflow: hidden; background: var(--backdrop); }
  .flier {
    position: absolute; left: 57px; top: 57px; width: 768px; height: 1086px;
    background: var(--paper); overflow: hidden;
    font-family: "Montserrat", Arial, sans-serif; color: var(--ink);
  }
  .masthead {
    position: absolute; left: 0; top: 0; width: 768px; height: 161px;
    background: radial-gradient(ellipse at 75% 90%, var(--night-glow), var(--night) 70%);
  }
  .brand-block {
    position: absolute; left: 33px; top: 0; width: 214px; height: 161px; background: #000;
    display: flex; align-items: center; justify-content: center; gap: 8px;
  }
  .brand-dot { width: 10px; height: 10px; border-radius: 50%; background: var(--logo); flex: none; }
  .brand-name {
    font-family: "Montserrat", Arial, sans-serif; font-weight: 600; font-size: 17px;
    line-height: 1.2; color: var(--logo); letter-spacing: 1px; text-transform: uppercase;
  }
  .headline {
    position: absolute; left: 294px; top: 42px; width: 460px;
    font-family: "Poppins", Arial, sans-serif; font-weight: 300; font-size: 35px;
    line-height: 31px; color: var(--white);
  }
  .service { position: absolute; width: 325px; }
  .service h2 {
    font-size: 15.5px; font-weight: 600; color: var(--heading); letter-spacing: 0.2px;
    padding-bottom: 4px; border-bottom: 3px solid var(--rule); margin-bottom: 10px;
  }
  .service p { font-size: 13px; line-height: 15.6px; font-weight: 400; }
  .billing { left: 46px; top: 214px; }
  .credentialing { left: 405px; top: 214px; }
  .aging { left: 46px; top: 416px; }
  .contact { left: 406px; top: 418px; }
  .scene { position: absolute; left: 0; top: 580px; width: 768px; height: 506px; }
  .contact-panel {
    position: absolute; left: 278px; top: 950px; width: 490px; height: 136px;
    background: linear-gradient(90deg, rgba(190,120,185,0.92), rgba(140,120,190,0.92));
    border-top-left-radius: 26px;
    padding: 14px 0 0 57px;
  }
  .contact-line {
    display: flex; align-items: center; gap: 12px; height: 31px;
    font-family: "Poppins", Arial, sans-serif; font-weight: 300; font-size: 20px; color: var(--white);
  }
  .contact-line svg { width: 18px; height: 18px; flex: none; }
</style>
</head>
<body>
<main class="flier">
  <header class="masthead">
    <div class="brand-block">
      <span class="brand-dot"></span>
      <span class="brand-name">Lyra<br>Medical Billing</span>
    </div>
    <h1 class="headline">Medical billing tailored to your practices needs</h1>
  </header>

  <section class="service billing">
    <h2>MEDICAL BILLING</h2>
    <p>Would you prefer to spend time focusing on your clients and running your practice rather than trying to stay up to speed with the constantly changing medical billing rules and regulations? Let us help you by managing your medical billing and dealing with the insurance companies on your behalf! We work with you to tailor the entire medical billing process to suit your practices needs while making it as smooth and painless as possible.</p>
  </section>

  <section class="service credentialing">
    <h2>CREDENTIALING</h2>
    <p>Are you wanting to get contracted with insurance companies but aren’t sure how to go about it? Are you wanting to expand your client base by having the option to bill insurance? Let us take the confusion out of what can seem like a daunting task! We can get you and your practitioners contracted with the insurance companies of your choice and help you navigate through the process every step of the way!</p>
  </section>

  <section class="service aging">
    <h2>AGING</h2>
    <p>Are you leaving money on the table? Are you able to do the follow-through needed to keep your aging in check and more money flowing into your practice? Are you uncertain about how to get insurance to pay on claims that should be covered but for some reason they decided not to? We can clean up your aging, reduce the amount of time it takes for claims to pay out, and we can keep your aging to a minimum.</p>
  </section>

  <section class="service contact">
    <h2>CONTACT US</h2>
    <p>If any of these processes are something you would like our help with or to consult with us on, please email us or give us a call! We specialize in billing and contracting for Nutritionists and Dietitians. We would love to help you expand your business and take the pain and frustration out of billing so you can focus on your clients.</p>
  </section>

  <svg class="scene" viewBox="0 0 768 506" aria-hidden="true">
    <defs>
      <linearGradient id="band" x1="0" x2="1" y1="0" y2="0">
        <stop offset="0" stop-color="#b464a8"/>
        <stop offset="1" stop-color="#6f63a8"/>
      </linearGradient>
      <linearGradient id="desk" x1="0" x2="0.6" y1="0" y2="1">
        <stop offset="0" stop-color="#eceef2"/>
        <stop offset="0.5" stop-color="#f7f8fa"/>
        <stop offset="1" stop-color="#d9dbe0"/>
      </linearGradient>
    </defs>
    <path d="M0 142 Q300 -40 768 40 L768 506 L0 506 Z" fill="url(#desk)" role="img" aria-label="Desk photo with a stethoscope, papers and a keyboard"/>
    <path d="M0 142 Q300 -40 768 40 L768 89 Q330 20 0 228 Z" fill="url(#band)"/>
  </svg>

  <address class="contact-panel">
    <div class="contact-line">
      <svg viewBox="0 0 24 24"><path fill="#fff" d="M6.6 2.5 9.5 7 7.6 9.2c1.3 2.9 3.5 5.2 6.4 6.6l2.1-2 4.6 2.8-1.6 4.3C11 20.4 3.7 13 3 4.1z"/></svg>
      <span>555-201-0188</span>
    </div>
    <div class="contact-line">
      <svg viewBox="0 0 24 24"><rect x="2" y="5" width="20" height="14" fill="none" stroke="#fff" stroke-width="2"/><path d="M2 5l10 8 10-8M2 19l7-7M22 19l-7-7" fill="none" stroke="#fff" stroke-width="2"/></svg>
      <span>admin@lyramedicalbilling.com</span>
    </div>
    <div class="contact-line">
      <svg viewBox="0 0 24 24" fill="none" stroke="#fff" stroke-width="1.8"><circle cx="12" cy="12" r="10"/><ellipse cx="12" cy="12" rx="4.5" ry="10"/><path d="M2 12h20M4 7h16M4 17h16"/></svg>
      <span>www.lyramedicalbilling.com</span>
    </div>
  </address>
</main>
</body>
</html>
```